WEBSITE NEEDED FOR MY COMPANY CALLED BRAMWORTH HOCKEY DEVELOPMENT

LOOKING FOR A WEBSITE TO MARKET AND SEEL MY HOCKEY DEVELOPMENT PROGRAMS.
NEEDS TO HAVE 5+ PAGES

Target Market(s)

YOUTH SPORTS

Industry/Entity Type

YOUTH ATHLETE DEVELOPMENT

Number of Pages Required

5+ page

Font styles to use
Sans Serif

Colors
0054AA
0677BA
7BADD7
CADEEF
E8F1F8

Requirements
Must have
• MAIN PAGE - SPIRNG PROGRAM PAGE - SUMMER PROGRAM PAGE - WINTER PAGE - TOURNAMENT PAGE
Nice to have
• FLASH
Should not have
• NOT SURE

```html
<!DOCTYPE html>
<html lang="en">
<head>
<meta charset="utf-8">
<title>Bramworth Hockey Development</title>
<link rel="stylesheet" href="https://fonts.googleapis.com/css2?family=Montserrat:wght@400;500;600;700;800&display=swap">
<style>
:root{
  --blue:#0a56b0;
  --blue-deep:#0054aa;
  --cyan:#2cbdee;
  --ink:#1d1f24;
  --text:#6b6f78;
  --navy:#0d1a33;
  --footer:#1e2230;
  --pale:#f2f6fb;
  --white:#fff;
}
*{box-sizing:border-box;margin:0;padding:0}
html,body{width:1200px;height:2995px;overflow:hidden;background:#fff;font-family:'Montserrat',sans-serif;color:var(--ink)}
.page{width:1200px;height:2995px;position:relative}
.btn{display:inline-block;background:var(--cyan);color:#fff;font-weight:700;font-size:12px;letter-spacing:.5px;border-radius:24px;text-align:center}

/* nav */
.nav{height:78px;display:flex;background:var(--blue)}
.nav-brand{width:300px;background:#fff;display:flex;align-items:center;justify-content:center;font-weight:800;font-size:17px;color:var(--blue-deep);letter-spacing:.5px}
.nav-menu{display:flex;align-items:center;gap:24px;padding-left:46px;list-style:none}
.nav-menu li{font-size:11px;color:#dbe8f7;font-weight:500}
.nav-menu li.active{color:var(--cyan)}
.nav-search{width:20px;height:20px;border-radius:50%;background:var(--cyan);margin-left:6px;display:flex;align-items:center;justify-content:center}

/* hero */
.hero{height:458px;position:relative;background:linear-gradient(120deg,#2d2b22 0%,#3c3626 40%,#23221d 70%,#3a3a36 100%);text-align:center;color:#fff}
.hero-title{padding-top:110px;font-size:38px;font-weight:800;line-height:45px}
.hero-title span{color:var(--cyan)}
.hero-text{font-size:12.5px;line-height:18px;margin-top:14px;color:#e9e9e9}
.hero .btn{width:174px;line-height:40px;margin-top:22px}
.dots{position:absolute;left:586px;top:402px;display:flex;gap:4px}
.dots i{width:6px;height:6px;border-radius:50%;background:#aaa}
.dots i:first-child{background:var(--cyan)}

/* welcome */
.welcome{height:384px;display:flex}
.welcome-photo{width:481px;background:linear-gradient(135deg,#0a2fd6,#0a1a8a 60%,#1a3cff)}
.welcome-body{position:relative;padding:72px 0 0 102px}
.side-label{position:absolute;left:55px;top:78px;writing-mode:vertical-rl;transform:rotate(180deg);font-size:8px;color:var(--blue);letter-spacing:.5px}
.side-label::after{content:"";display:block;width:2px;height:36px;background:var(--blue);margin-top:6px}
.welcome h2{font-size:23px;font-weight:800;line-height:29px}
.welcome p{width:430px;font-size:11.5px;line-height:19.3px;color:var(--text);text-align:justify;margin-top:20px}
.welcome .btn{width:174px;line-height:40px;margin-top:26px}

/* programs */
.programs{height:317px;display:flex}
.program{flex:1;position:relative}
.program:nth-child(1){background:linear-gradient(135deg,#c22b2b,#e8e8ea 55%,#9ba0a8)}
.program:nth-child(2){background:linear-gradient(135deg,#4f3a3a,#3b5a35 55%,#6d7a62)}
.program:nth-child(3){background:linear-gradient(135deg,#f3f3f3,#1b1b1d 50%,#ededed)}
.program-caption{position:absolute;left:0;right:0;bottom:0;height:123px;background:rgba(28,30,36,.86);color:#fff;text-align:center;padding-top:14px}
.program-caption h3{font-size:17px;font-weight:800}
.program-caption p{font-size:11px;line-height:16px;margin-top:5px;color:#e2e2e2}
.program-caption .btn{width:116px;line-height:24px;font-size:8px;margin-top:9px}

/* improvement */
.improve{height:367px;text-align:center}
.improve h2{padding-top:82px;font-size:22px;font-weight:800}
.skills{display:flex;justify-content:center;gap:40px;margin-top:52px;list-style:none}
.skills li{width:96px;font-size:11.5px;font-weight:700}
.ring{width:96px;height:96px;border-radius:50%;border:2px solid var(--blue);display:flex;align-items:center;justify-content:center;margin-bottom:14px}
.ring span{width:82px;height:82px;border-radius:50%;background:var(--blue);display:flex;align-items:center;justify-content:center}

/* tournament */
.tournament{height:349px;position:relative;background:linear-gradient(180deg,#0b1830,#132544 55%,#1d2430)}
.tournament-photo{position:absolute;left:550px;top:30px;width:540px;height:319px;background:radial-gradient(ellipse at 50% 55%,#33476e,rgba(19,37,68,0) 70%)}
.tournament-copy{position:absolute;left:150px;top:75px;width:430px;color:#fff}
.tournament h2{font-size:23px;font-weight:800}
.tournament p{font-size:11.5px;line-height:19.3px;text-align:justify;margin-top:10px;color:#e6e9ef}
.tournament .btn{width:174px;line-height:40px;margin-top:22px}
.team{position:absolute;left:780px;color:#fff;font-size:19px;font-weight:800}
.vs{position:absolute;left:808px;top:156px;width:26px;height:26px;border-radius:50%;background:var(--cyan);color:#fff;font-size:8px;font-weight:700;text-align:center;line-height:26px}

/* alumni */
.alumni{height:331px;text-align:center}
.alumni h2{padding-top:63px;font-size:22px;font-weight:800}
.reviews{display:flex;gap:10px;padding-left:150px;margin-top:28px;text-align:left}
.review{width:294px}
.review-head{display:flex;height:60px}
.review-face{width:86px;background:linear-gradient(#e9ecef,#cfd5dc)}
.review-name{flex:1;background:var(--blue);display:flex;align-items:center;gap:10px;padding-left:8px;color:#fff}
.quote{width:30px;height:30px;border-radius:50%;background:var(--cyan);display:flex;align-items:center;justify-content:center}
.review-name b{display:block;font-size:12.5px;font-weight:700}
.review-name small{font-size:11.5px}
.review p{font-size:11.5px;line-height:19px;color:var(--text);margin-top:12px}

/* location */
.location{height:346px;display:flex;background:var(--pale)}
.location-copy{width:612px;padding:96px 0 0 150px}
.location h2{font-size:22px;font-weight:800}
.location p{width:420px;font-size:11px;line-height:18px;color:var(--text);margin-top:10px}
.contact{list-style:none;margin-top:14px}
.contact li{display:flex;align-items:center;gap:8px;font-size:13px;color:#4a4e57;height:30px}
.contact i{width:20px;height:20px;border-radius:50%;background:var(--blue);display:flex;align-items:center;justify-content:center}
.map{flex:1;background:linear-gradient(135deg,#efe9dc,#e3e7ea 50%,#ece4d3)}

/* footer */
.footer{height:365px;background:var(--footer);text-align:center;color:#b9bfca}
.footer-brand{padding-top:80px;font-size:24px;font-weight:800;color:var(--cyan);letter-spacing:.5px}
.social{display:flex;justify-content:center;gap:12px;margin-top:50px}
.social i{width:28px;height:28px;background:#2f3444;border-radius:3px}
.footer-menu{display:flex;justify-content:center;gap:18px;list-style:none;margin-top:32px;font-size:9.5px}
.copy{font-size:9.5px;margin-top:18px}
</style>
</head>
<body>
<div class="page">

  <header class="nav">
    <div class="nav-brand">BRAMWORTH HOCKEY</div>
    <ul class="nav-menu">
      <li class="active">HOME</li><li>SPIRNG PROGRAM</li><li>SUMMER PROGRAM</li><li>WINTER PROGRAM</li><li>TOURNAMENT</li><li>CONTACT US</li>
      <li class="nav-search"><svg width="10" height="10" viewBox="0 0 10 10"><circle cx="4" cy="4" r="3" fill="none" stroke="#fff" stroke-width="1.4"/><path d="M6.3 6.3 9 9" stroke="#fff" stroke-width="1.4"/></svg></li>
    </ul>
  </header>

  <section class="hero" role="img" aria-label="Youth hockey players battling for the puck at a faceoff with a referee">
    <h1 class="hero-title"><span>DEVELOP</span> THE PLAYER.<br>DEVELOP THE GAME.</h1>
    <p class="hero-text">Lorem Ipsum is simply dummy text of the printing and typesetting<br>industry. Lorem Ipsum has been the industry's standard</p>
    <a class="btn">GAME ON</a>
    <div class="dots"><i></i><i></i><i></i></div>
  </section>

  <section class="welcome">
    <div class="welcome-photo" role="img" aria-label="Blue-tinted arena boards and ice surface"></div>
    <div class="welcome-body">
      <span class="side-label">ABOUT US</span>
      <h2>WELCOME TO<br>BRAMWORTH HOCKEY DEVELOPMENT</h2>
      <p>Lorem Ipsum is simply dummy text of the printing and typesetting industry. Lorem Ipsum has been the industry's standard dummy text ever since the 1500s, when an unknown printer took a galley of type and scrambled it to make a type specimen book. It has survived not only five centuries, but also the leap into electronic typesetting, remaining essentially unchanged.</p>
      <a class="btn">LEARN MORE</a>
    </div>
  </section>

  <section class="programs">
    <article class="program" role="img" aria-label="Two players in red and white jerseys during a spring game">
      <div class="program-caption"><h3>SPIRNG PROGRAM</h3><p>Lorem Ipsum is simply dummy text<br>of the printing and typesetting .</p><a class="btn">LEARN MORE</a></div>
    </article>
    <article class="program" role="img" aria-label="Outdoor summer field game beside a championship banner">
      <div class="program-caption"><h3>SUMMER PROGRAM</h3><p>Lorem Ipsum is simply dummy text<br>of the printing and typesetting .</p><a class="btn">LEARN MORE</a></div>
    </article>
    <article class="program" role="img" aria-label="Players in black and white jerseys contesting the puck on ice">
      <div class="program-caption"><h3>WINTER PROGRAM</h3><p>Lorem Ipsum is simply dummy text<br>of the printing and typesetting .</p><a class="btn">LEARN MORE</a></div>
    </article>
  </section>

  <section class="improve">
    <h2>CONTINUOUS IMPROVEMENT</h2>
    <ul class="skills">
      <li><div class="ring"><span><svg width="28" height="28" viewBox="0 0 28 28"><path d="M8 8l6 12 6-12" fill="none" stroke="#fff" stroke-width="2"/></svg></span></div>RETENTION</li>
      <li><div class="ring"><span><svg width="28" height="28" viewBox="0 0 28 28"><path d="M18 6l-6 14h-4" fill="none" stroke="#fff" stroke-width="2"/></svg></span></div>TECHNIQUE</li>
      <li><div class="ring"><span><svg width="28" height="28" viewBox="0 0 28 28"><path d="M6 14h16M14 10v8" fill="none" stroke="#fff" stroke-width="2"/></svg></span></div>REFLEX</li>
      <li><div class="ring"><span><svg width="28" height="28" viewBox="0 0 28 28"><path d="M9 7v12h11" fill="none" stroke="#fff" stroke-width="2"/></svg></span></div>AGILITY</li>
      <li><div class="ring"><span><svg width="28" height="28" viewBox="0 0 28 28"><path d="M14 6v14M8 20h12" fill="none" stroke="#fff" stroke-width="2"/></svg></span></div>CONTROL</li>
    </ul>
  </section>

  <section class="tournament">
    <div class="tournament-photo" role="img" aria-label="Two skaters from opposing teams facing each other in an arena"></div>
    <div class="tournament-copy">
      <h2>TOURNAMENT</h2>
      <p>Lorem Ipsum is simply dummy text of the printing and typesetting industry. Lorem Ipsum has been the industry's standard dummy text ever since the 1500s, when an unknown printer took a galley of type and scrambled it to make a type specimen book. It has survived not only five centuries, but also the leap into electronic typesetting, remaining essentially unchanged.</p>
      <a class="btn">LEARN MORE</a>
    </div>
    <div class="team" style="top:110px">TEAM-A</div>
    <div class="vs">VS</div>
    <div class="team" style="top:192px">TEAM-B</div>
  </section>

  <section class="alumni">
    <h2>SEE WHAT OUR ALUMNI ARE SAYING</h2>
    <div class="reviews">
      <article class="review">
        <div class="review-head"><div class="review-face" role="img" aria-label="Portrait of Owen Marlowe"></div><div class="review-name"><span class="quote"><svg width="12" height="10" viewBox="0 0 12 10"><path d="M0 10V5L3 0h2L3 5h2v5zM7 10V5l3-5h2l-2 5h2v5z" fill="#fff"/></svg></span><div><b>OWEN MARLOWE</b><small>Lorem Ipsum</small></div></div></div>
        <p>Lorem Ipsum is simply dummy text of the printing and typesetting industry. It is a long established fact that a reader will be</p>
      </article>
      <article class="review">
        <div class="review-head"><div class="review-face" role="img" aria-label="Portrait of Lucas Trembley"></div><div class="review-name"><span class="quote"><svg width="12" height="10" viewBox="0 0 12 10"><path d="M0 10V5L3 0h2L3 5h2v5zM7 10V5l3-5h2l-2 5h2v5z" fill="#fff"/></svg></span><div><b>LUCAS TREMBLEY</b><small>Lorem Ipsum</small></div></div></div>
        <p>Lorem Ipsum is simply dummy text of the printing and typesetting industry. It is a long established fact that a reader will be</p>
      </article>
      <article class="review">
        <div class="review-head"><div class="review-face" role="img" aria-label="Portrait of Noah Halversen"></div><div class="review-name"><span class="quote"><svg width="12" height="10" viewBox="0 0 12 10"><path d="M0 10V5L3 0h2L3 5h2v5zM7 10V5l3-5h2l-2 5h2v5z" fill="#fff"/></svg></span><div><b>NOAH HALVERSEN</b><small>Lorem Ipsum</small></div></div></div>
        <p>Lorem Ipsum is simply dummy text of the printing and typesetting industry. It is a long established fact that a reader will be</p>
      </article>
    </div>
  </section>

  <section class="location">
    <div class="location-copy">
      <h2>LOCATION &amp; CONTACT</h2>
      <p>Lorem Ipsum is simply dummy text of the printing and typesetting industry. It is a long established fact that a reader will be</p>
      <ul class="contact">
        <li><i><svg width="10" height="10" viewBox="0 0 10 10"><path d="M2 1l2 2-1 1.5c.8 1.3 1.5 2 2.5 2.5L7 6l2 2-1.2 1.5C4.5 9 1 5.5.5 2.2z" fill="#fff"/></svg></i>1 (800) 555-0142</li>
        <li><i><svg width="10" height="8" viewBox="0 0 10 8"><rect x=".5" y=".5" width="9" height="7" fill="none" stroke="#fff"/><path d="M.5.5 5 4.5 9.5.5" fill="none" stroke="#fff"/></svg></i>hello@bramworthhockey.test</li>
        <li><i><svg width="8" height="11" viewBox="0 0 8 11"><path d="M4 11S0 6.5 0 4a4 4 0 0 1 8 0c0 2.5-4 7-4 7z" fill="#fff"/><circle cx="4" cy="4" r="1.5" fill="#0a56b0"/></svg></i>48 Rinkside Avenue, 3C, Millbrook, NY 10990</li>
      </ul>
    </div>
    <div class="map" role="img" aria-label="Street map showing the facility location"></div>
  </section>

  <footer class="footer">
    <div class="footer-brand">BRAMWORTH HOCKEY DEVELOPMENT</div>
    <div class="social"><i></i><i></i><i></i><i></i></div>
    <ul class="footer-menu"><li>HOME</li><li>SPIRNG PROGRAM</li><li>SUMMER PROGRAM</li><li>WINTER PROGRAM</li><li>TOURNAMENT</li><li>CONTACT US</li></ul>
    <p class="copy">© 2020 BRAMWORTH HOCKEY DEVELOPMENT</p>
  </footer>

</div>
</body>
</html>
```